Business Card Design Project

Use our current logo. Clean design.

Industry/Entity Type

Business

Requirements
Must have
• Marisela DUBRANCQ
M. Law
Managing Partner

Alpenvorsa AG
Kornhalmweg 214
CH-3097 Liebefeld

M. +41 79 412 56 27
T. +41 31 928 44 10
F. +41 31 928 44 19

m.dubrancq@alpenvorsa-example.com
www.alpenvorsa-example.com

```html
<!DOCTYPE html>
<html lang="de">
<head>
<meta charset="utf-8">
<title>Alpenvorsa – Visitenkarte</title>
<link rel="stylesheet" href="https://fonts.googleapis.com/css2?family=Open+Sans:wght@400;600&display=swap">
<style>
  :root {
    --backdrop: #e6e6e6;
    --card-beige: #b6a893;
    --ink: #1c1a18;
    --frame-black: #1a1a1a;
    --shadow: rgba(0, 0, 0, 0.18);
  }
  * { box-sizing: border-box; margin: 0; padding: 0; }
  html, body {
    width: 1200px;
    height: 900px;
    overflow: hidden;
  }
  body {
    background: var(--backdrop);
    font-family: "Open Sans", Arial, sans-serif;
    color: var(--ink);
    display: flex;
    align-items: center;
    justify-content: center;
    gap: 60px;
  }
  .card {
    width: 520px;
    height: 336px;
    background: var(--card-beige);
    box-shadow: 0 10px 28px var(--shadow);
    position: relative;
  }

  /* Front side */
  .card--front .inner-frame {
    position: absolute;
    inset: 22px;
    border: 1.5px solid var(--ink);
    display: flex;
    align-items: center;
    justify-content: center;
  }
  .brand-name {
    font-size: 40px;
    font-weight: 400;
    letter-spacing: 5px;
    color: var(--ink);
  }

  /* Back side */
  .card--back {
    border: 16px solid var(--frame-black);
    display: flex;
    padding: 28px 26px;
    font-size: 13.5px;
    line-height: 1.45;
  }
  .person {
    width: 42%;
    padding-right: 18px;
  }
  .person-name {
    font-size: 16px;
    font-weight: 400;
    letter-spacing: 0.3px;
  }
  .person-role { margin-top: 2px; }
  .divider {
    width: 1px;
    background: var(--ink);
    align-self: stretch;
    margin: 0 18px 0 0;
  }
  .contact { flex: 1; }
  .contact-block + .contact-block { margin-top: 14px; }
  .phone-line {
    display: flex;
    align-items: center;
    gap: 8px;
  }
  .phone-icon {
    width: 12px;
    height: 12px;
    flex: none;
  }
</style>
</head>
<body>

  <section class="card card--front" aria-label="Visitenkarte Vorderseite">
    <div class="inner-frame">
      <span class="brand-name">ALPENVORSA</span>
    </div>
  </section>

  <section class="card card--back" aria-label="Visitenkarte Rückseite">
    <div class="person">
      <p class="person-name">Marisela DUBRANCQ</p>
      <p class="person-role">M. Law</p>
      <p class="person-role">Managing Partner</p>
    </div>
    <div class="divider"></div>
    <div class="contact">
      <div class="contact-block">
        <p>Alpenvorsa AG</p>
        <p>Kornhalmweg 214</p>
        <p>CH-3097 Liebefeld</p>
      </div>
      <div class="contact-block">
        <p class="phone-line">
          <svg class="phone-icon" viewBox="0 0 12 12" aria-label="Mobil"><rect x="2.5" y="0.5" width="7" height="11" rx="1.5" fill="var(--ink)"/><rect x="3.8" y="2" width="4.4" height="7" fill="var(--card-beige)"/></svg>
          +41 79 412 56 27
        </p>
        <p class="phone-line">
          <svg class="phone-icon" viewBox="0 0 12 12" aria-label="Telefon"><path d="M2 1.2 L4.2 1 L5.2 3.6 L3.9 4.6 Q5 7 7.4 8.1 L8.4 6.8 L11 7.8 L10.8 10 Q10.4 11 9.2 11 Q1 10.2 1 2.8 Q1 1.6 2 1.2 Z" fill="var(--ink)"/></svg>
          +41 31 928 44 10
        </p>
        <p class="phone-line">
          <svg class="phone-icon" viewBox="0 0 12 12" aria-label="Fax"><rect x="1" y="4.5" width="10" height="6" rx="1" fill="var(--ink)"/><rect x="3" y="1" width="6" height="4" fill="var(--ink)"/><rect x="3.8" y="6.5" width="4.4" height="1" fill="var(--card-beige)"/></svg>
          +41 31 928 44 19
        </p>
      </div>
      <div class="contact-block">
        <p>m.dubrancq@alpenvorsa-example.com</p>
        <p>www.alpenvorsa-example.com</p>
      </div>
    </div>
  </section>

</body>
</html>
```